Awaken the Quiet Summit is a guide to help individuals overcome obstacles that they face in their life. This book provides thought provoking concepts that allow individuals to work through challenges if their life. The cover needs to be powerful! It needs to speak to the reader of breaking free of problems and overcoming challenges.

Awaken The Quiet Summit
A Map for climbing past hardship and stepping toward the self you were always built to become.
By
Dr. Merrick T. Halvorsby

Industry/Entity Type

Work

```html
<!DOCTYPE html>
<html lang="en">
<head>
<meta charset="utf-8">
<title>Awaken The Quiet Summit — Book Cover</title>
<link rel="stylesheet" href="https://fonts.googleapis.com/css2?family=Cinzel:wght@500;600&family=Open+Sans:wdth,wght@75..100,400..700&display=swap">
<style>
  :root {
    --navy-deep: #061226;
    --navy: #0e2548;
    --navy-mid: #1d3f6e;
    --spine-top: #1c3a67;
    --spine-bottom: #2a4d7c;
    --sky-top: #2e4f7a;
    --sky: #6f93bf;
    --crimson: #b0173f;
    --ink: #050505;
    --white: #ffffff;
    --shadow: rgba(0, 0, 0, 0.85);
  }
  * { box-sizing: border-box; margin: 0; padding: 0; }
  html, body { width: 1200px; height: 900px; overflow: hidden; background: var(--navy-deep); }
  .cover-wrap { position: relative; width: 1200px; height: 900px; overflow: hidden; }

  /* Back cover */
  .back-cover {
    position: absolute; left: 0; top: 0; width: 540px; height: 900px;
    background: radial-gradient(ellipse at 55% 45%, var(--navy-mid) 0%, var(--navy) 55%, var(--navy-deep) 100%);
  }
  .blurb, .author-profile {
    position: absolute; left: 48px; width: 452px; text-align: center;
    font-family: "Open Sans", sans-serif; font-stretch: 75%; font-weight: 400;
    font-size: 19px; line-height: 27px; color: var(--white);
  }
  .blurb { top: 199px; }
  .author-profile { top: 595px; }
  .author-profile h2 { font-size: 19px; font-weight: 400; line-height: 27px; margin-bottom: 6px; }
  .barcode-box {
    position: absolute; left: 412px; top: 828px; width: 110px; height: 54px;
    background: var(--white); color: var(--ink); text-align: center;
    font-family: "Open Sans", sans-serif; font-weight: 500; font-size: 20px; line-height: 24px;
    padding-top: 3px;
  }

  /* Spine */
  .spine {
    position: absolute; left: 540px; top: 0; width: 92px; height: 900px;
    background: linear-gradient(180deg, var(--spine-top) 0%, var(--navy-mid) 50%, var(--spine-bottom) 100%);
  }
  .spine-rule { position: absolute; left: 43px; top: 64px; width: 3px; height: 706px; background: var(--white); }
  .spine-title {
    position: absolute; left: 48px; top: 66px; height: 700px;
    writing-mode: vertical-rl; font-family: "Cinzel", serif; font-weight: 600;
    font-size: 40px; line-height: 40px; color: var(--crimson); white-space: nowrap;
    text-shadow: -2px 2px 2px var(--shadow);
  }
  .spine-subtitle {
    position: absolute; left: 2px; top: 150px; width: 40px; height: 620px;
    writing-mode: vertical-rl; font-family: "Open Sans", sans-serif; font-stretch: 75%;
    font-weight: 500; font-size: 15px; line-height: 20px; color: var(--ink); text-transform: uppercase;
  }
  .spine-author {
    position: absolute; left: 0; top: 800px; width: 92px; text-align: center;
    font-family: "Open Sans", sans-serif; font-stretch: 75%; font-weight: 500;
    font-size: 18px; line-height: 26px; color: var(--ink); text-transform: uppercase;
  }

  /* Front cover */
  .front-cover {
    position: absolute; left: 632px; top: 0; width: 568px; height: 900px;
    background: linear-gradient(180deg, var(--navy-deep) 0%, var(--navy) 20%, var(--sky-top) 45%, #4a6d99 80%, #2c4b76 100%);
    border-left: 1px solid rgba(255,255,255,0.25);
  }
  .title {
    position: absolute; left: 0; top: 68px; width: 568px; text-align: center;
    font-family: "Cinzel", serif; font-weight: 600; font-size: 74px; line-height: 74px;
    color: var(--crimson); text-shadow: -5px 5px 4px var(--shadow);
  }
  .title-rule { position: absolute; left: 40px; top: 298px; width: 480px; height: 4px; background: var(--white); }
  .subtitle {
    position: absolute; left: 20px; top: 313px; width: 528px; text-align: center;
    font-family: "Open Sans", sans-serif; font-stretch: 75%; font-weight: 600;
    font-size: 26px; line-height: 32px; color: var(--white); text-transform: uppercase;
    text-shadow: -3px 3px 3px var(--shadow);
  }
  .hero-photo { position: absolute; left: 0; top: 420px; width: 568px; height: 390px; }
  .author {
    position: absolute; left: 0; top: 846px; width: 568px; text-align: center;
    font-family: "Open Sans", sans-serif; font-stretch: 75%; font-weight: 400;
    font-size: 40px; line-height: 48px; letter-spacing: 2px; color: var(--white);
  }
</style>
</head>
<body>
<main class="cover-wrap">
  <section class="back-cover">
    <p class="blurb">Awaken the Quiet Summit is a guide to help individuals overcome obstacles that they face in their life. This book provides thought provoking concepts that allow individuals to work through challenges if their life. The cover needs to be powerful! It needs to speak to the reader of breaking free of problems and overcoming challenges.</p>
    <div class="author-profile">
      <h2>AUTHOR’S PROFILE</h2>
      <p>Awaken the Quiet Summit is a guide to help individuals overcome obstacles that they face in their life. This book provides thought provoking concepts that allow individuals to work through challenges if their life. The cover needs to be</p>
    </div>
    <div class="barcode-box">BAR<br>CODE</div>
  </section>

  <section class="spine">
    <div class="spine-subtitle">A Map for climbing past hardship and stepping toward the self you were always built to become</div>
    <div class="spine-rule"></div>
    <div class="spine-title">Awaken The Quiet Summit</div>
    <div class="spine-author">Dr.<br>Merrick T.<br>Halvorsby</div>
  </section>

  <section class="front-cover">
    <h1 class="title">Awaken The<br>Quiet<br>Summit</h1>
    <div class="title-rule"></div>
    <p class="subtitle">A Map for climbing past hardship and stepping toward the self you were always built to become</p>
    <svg class="hero-photo" role="img" aria-label="Photograph of a torn chain-link fence against a bright cloudy blue sky" viewBox="0 0 568 390" preserveAspectRatio="none">
      <defs>
        <linearGradient id="skyFade" x1="0" y1="0" x2="0" y2="1">
          <stop offset="0" stop-color="#2e4f7a" stop-opacity="0"/>
          <stop offset="0.15" stop-color="#5b7fab"/>
          <stop offset="0.55" stop-color="#9cb6d4"/>
          <stop offset="0.85" stop-color="#5f85b3"/>
          <stop offset="1" stop-color="#3b5e8b" stop-opacity="0"/>
        </linearGradient>
      </defs>
      <rect width="568" height="390" fill="url(#skyFade)"/>
    </svg>
    <p class="author">DR. MERRICK T. HALVORSBY</p>
  </section>
</main>
</body>
</html>
```